Business card design needed

Family General Practitioner/ Family Physician.
Logo is the logo of the Crestmoor Guild of Family Clinicians Australia
http://kvplm.tarevo.edu.au/PictureGallery/logos/pages/CGFC%20logo_jpg.htm

Reason: Just a bit more time to make changes and the weekend for me to look at things closely and to choose. Thanks, Lumi

Thanks for all the submissions. So many of them are really works of art. Not one of them are not good. The ones that I am eliminating are the ones that I think are not suitable for me personally only, and because if I don't, it makes it very difficult to decide as many of you are also sending me slight variations of a card. I have just decided to choose a second place card too. Can't thank you all enough. Good luck, Lumi. P.S - Working today till 10 pm as the card says :-), so probably won't be able to give a feedback till late Saturday night or Sunday morning here in Sydney, Australia. 

Reason: Just added a second place to the budget and realised that Australia is ahead of the rest of the world in the time zone (only :-) - don't want to offend anyone or start a debate!! ) , so Monday deadline will mean it will be a weekend for the rest of the world. Just wanted to give everyone more time to submit their best, especially since I will be picking a second card too. Can't thank everyone enough for the submissions. P.S - Not keen on photos on the card.

Contact Information for Business Card

Dr. Lumi Harcourt M.B.B.S., F.C.G.F.C
Family General Practitioner
Address, timings, phone and fax number on the back.

Requirements
Must have
• Timings
Mon 7 am - 7 pm
Tues 7 am - 12 pm
Wed 7 am - 10 pm
Thurs 7 am - 12 pm
Fri 7 am - 8 pm
Sat 8 am - 10 pm
Sun - Off

```html
<!DOCTYPE html>
<html lang="en">
<head>
<meta charset="utf-8">
<title>Dr. Lumi Harcourt – Business Card</title>
<link rel="stylesheet" href="https://fonts.googleapis.com/css2?family=Righteous&family=Tinos&family=Questrial&display=swap">
<style>
  :root {
    --page: #ffffff;
    --cream: #f3f0ed;
    --navy: #0d3f63;
    --ink: #111111;
    --blue-deep: #0a8fd0;
    --blue-mid: #2aa9e2;
    --blue-soft: #8dcdf0;
    --blue-pale: #cfe9f8;
    --white: #ffffff;
    --address: #1f4f7a;
  }
  html, body {
    margin: 0;
    padding: 0;
    width: 1000px;
    height: 1200px;
    overflow: hidden;
    background: var(--page);
  }
  .canvas {
    position: relative;
    width: 1000px;
    height: 1200px;
  }
  .card {
    position: absolute;
    left: 172px;
    width: 656px;
    overflow: hidden;
    background: var(--cream);
  }
  .card--front { top: 202px; height: 379px; }
  .card--back  { top: 618px; height: 380px; outline: 1px solid #d5e6f2; }

  .front-wave-area {
    position: absolute;
    inset: 0;
    width: 656px;
    height: 379px;
  }
  .doctor-name {
    position: absolute;
    left: 50px;
    top: 62px;
    margin: 0;
    font-family: "Righteous", sans-serif;
    font-weight: 400;
    font-size: 40px;
    line-height: 1;
    color: var(--navy);
    letter-spacing: 0.5px;
    white-space: nowrap;
  }
  .credentials {
    position: absolute;
    left: 142px;
    top: 110px;
    margin: 0;
    font-family: "Tinos", serif;
    font-size: 15px;
    color: var(--ink);
    letter-spacing: 1.2px;
    white-space: nowrap;
  }
  .role {
    position: absolute;
    left: 72px;
    top: 136px;
    margin: 0;
    font-family: "Tinos", serif;
    font-size: 26px;
    color: var(--ink);
    white-space: nowrap;
  }
  .guild-mark {
    position: absolute;
    left: 446px;
    top: 168px;
    display: flex;
    align-items: center;
    gap: 8px;
    font-family: "Righteous", sans-serif;
    font-size: 30px;
    line-height: 1;
    color: var(--navy);
  }
  .guild-mark__dot {
    width: 22px;
    height: 22px;
    border-radius: 50%;
    background: var(--navy);
  }

  .hours-panel {
    position: absolute;
    left: 0;
    top: 0;
    width: 656px;
    height: 266px;
    background: radial-gradient(ellipse 60% 75% at 45% 45%, var(--blue-soft) 0%, var(--blue-mid) 65%, var(--blue-deep) 100%);
  }
  .hours-title {
    position: absolute;
    left: 52px;
    top: 40px;
    margin: 0;
    font-family: "Righteous", sans-serif;
    font-weight: 400;
    font-size: 27px;
    color: var(--navy);
    white-space: nowrap;
  }
  .hours-list {
    position: absolute;
    right: 46px;
    top: 39px;
    margin: 0;
    padding: 0;
    list-style: none;
    text-align: right;
    font-family: "Righteous", sans-serif;
    font-size: 23px;
    line-height: 30px;
    color: var(--white);
    white-space: nowrap;
  }
  .contact {
    position: absolute;
    left: 35px;
    top: 282px;
    font-style: normal;
    font-family: "Questrial", sans-serif;
    font-size: 15.5px;
    line-height: 19px;
    color: var(--address);
    white-space: nowrap;
  }
  .contact p { margin: 0; }
  .contact .phones { margin-top: 9px; }
</style>
</head>
<body>
<main class="canvas">

  <section class="card card--front" aria-label="Business card front">
    <svg class="front-wave-area" viewBox="0 0 656 379" role="img" aria-label="Decorative blue wave swirl sweeping along the right side and bottom of the card">
      <defs>
        <linearGradient id="waveTone" x1="0" y1="0" x2="1" y2="1">
          <stop offset="0" stop-color="#a8daf4"/>
          <stop offset="0.5" stop-color="#5cbce9"/>
          <stop offset="1" stop-color="#1a9fda"/>
        </linearGradient>
      </defs>
      <path d="M340 0 H656 V379 H0 V262 C60 200 180 200 280 250 C380 300 500 320 580 292 C640 262 645 150 570 80 C505 30 420 10 340 0 Z" fill="url(#waveTone)"/>
    </svg>

    <h1 class="doctor-name">Dr. Lumi Harcourt</h1>
    <p class="credentials">M.B.B.S., F.C.G.F.C</p>
    <p class="role">Family General Practitioner</p>
    <div class="guild-mark"><span class="guild-mark__dot"></span>CGFC</div>
  </section>

  <section class="card card--back" aria-label="Business card back">
    <div class="hours-panel">
      <h2 class="hours-title">Working Hours</h2>
      <ul class="hours-list">
        <li>Mon 7 am - 7 pm</li>
        <li>Tues 7 am - 12 pm</li>
        <li>Wed 7 am - 10 pm</li>
        <li>Thurs 7 am - 12 pm</li>
        <li>Fri 7 am - 8 pm</li>
        <li>Sat 8 am - 10 pm</li>
        <li>Sunday OFF</li>
      </ul>
    </div>
    <address class="contact">
      <p>Upper Level, Fountain Walk, Larkfield Arcade</p>
      <p>Brookvale Heights, NSW 2199</p>
      <p class="phones">P: 02 5550 1400 F: 02 5550 1233</p>
    </address>
  </section>

</main>
</body>
</html>
```